Corwith Lodge website redesign

After 8 years of our current site, we're ready to upgrade our site design. We'd like to generally make it more modern and clean and build it on a CMS like joomla for easier future maintenance.

Our hotel is a family-owned bed and breakfast that competes against much larger hotel chains in Aspen with fancier rooms and larger pricetags. Our hotel is priced moderately and features tasteful, uniquely-design rooms.

We are looking for a website that will showcase the uniqueness of our rooms, the history of the Lodge, and the friendliness of our staff.

Here are some other hotel sites we like:

http://www.brackenfoldhouse.example/

http://www.tollerpeakhaus.example/

http://www.quarrowstay.example/

*********

Scope of Work - I'm looking for a design AND build. The website should be built out in Joomla as part of the final deliverable.
Updates

Current website: http://www.corwithlodge.example/

Explanation of what design + build means:

I am looking for not only the design of the site, but also for the homepage and one subpage to be built out as well. I do NOT need the entire site built - only for those two pages to be built and I will retrofit the remainder of the pages.

Target Market(s)

travellers evaluating hotels in Aspen, Colorado.

Industry/Entity Type

Hotel

Requirements
Must have
• Must, must, must be based on a joomla template. "Rotating" large main image as central position on homepage is a must (see example websites mentioned above).

Nice to have
• We have an existing online reservation system. It would be nice to evaluate placing a "widget" on the homepage that integrates to the online reservation page. Similar to that feature that the Bracken Fold website has at the foot of the main image on their homepage.

```html
<!DOCTYPE html>
<html lang="en">
<head>
<meta charset="utf-8">
<title>Corwith Lodge – Aspen Bed &amp; Breakfast</title>
<link rel="stylesheet" href="https://fonts.googleapis.com/css2?family=Rosarivo&family=Quattrocento+Sans:wght@400;700&family=Arimo:wght@400;700&family=Dancing+Script:wght@500&family=Josefin+Sans:wght@300;400&display=swap">
<style>
:root{
  --paper:#e6e3d6;
  --page:#e2e8d2;
  --rust:#8c2e17;
  --rust-light:#a9452a;
  --rust-dark:#6e1f0c;
  --brown-text:#5a4a3a;
  --muted:#7c7466;
  --olive:#6a7a12;
  --offer-green:#8db52a;
  --offer-orange:#f08a16;
  --panel-dark:#2b2624;
  --panel-band:#1f1b19;
  --gold:#e8a13a;
  --orange:#f07a1a;
  --white:#ffffff;
}
*{box-sizing:border-box;margin:0;padding:0}
html,body{width:1138px;height:1200px;overflow:hidden}
body{background:var(--page);font-family:"Rosarivo",serif;color:var(--muted);position:relative}

.site-header{position:absolute;left:0;top:0;width:1138px;height:172px;background:var(--paper)}
.brand{position:absolute;top:42px;width:100%;text-align:center;font-family:"Rosarivo",serif;font-size:54px;color:#6b665e;letter-spacing:1px}
.tagline{position:absolute;top:127px;width:100%;text-align:center;font-family:"Quattrocento Sans",sans-serif;font-size:12px;color:#6a645a}
.social{position:absolute;top:139px;left:924px;display:flex;gap:8px}
.social span{width:26px;height:26px;border-radius:50%;background:#6a8ab8;border:2px solid #d8d8d8;display:block}
.social span:first-child{background:#4aa8d8}

.main-nav{position:absolute;top:172px;left:0;width:1138px;height:35px;background:linear-gradient(#a8432a,#7e2410);border-bottom:1px solid #5a1808}
.main-nav ul{list-style:none;display:flex;margin-left:142px}
.main-nav li{height:35px;display:flex;align-items:center;justify-content:center;font-family:"Arimo",sans-serif;font-size:12px;color:var(--white);border-right:1px solid #6a1c0a}
.main-nav li.active{background:linear-gradient(#8e8a86,#5f5a56)}

.hero{position:absolute;left:141px;top:217px;width:855px;height:427px;background:#dcd9d0;border:1px solid #b8b4aa}
.hero-photo{position:absolute;left:8px;top:5px;width:839px;height:314px;background:linear-gradient(160deg,#e8ecef 0%,#8a7560 35%,#6d4c36 60%,#c9b6a0 85%,#f2f2f2 100%)}
.offer{position:absolute;left:0;bottom:0;width:530px;height:92px;background:rgba(40,32,28,.72);padding:8px 15px;color:var(--white)}
.offer h2{font-family:"Arimo",sans-serif;font-size:23px;color:var(--offer-green);line-height:24px}
.offer h3{font-family:"Arimo",sans-serif;font-size:11px;font-weight:400;color:var(--offer-orange);margin-bottom:8px}
.offer p{font-family:"Arimo",sans-serif;font-size:9px;line-height:12px}
.offer a{color:#b0b8a0;text-decoration:none}
.thumbs{position:absolute;left:8px;top:325px;width:839px;height:92px;border-top:1px solid #c4c0b6;display:flex;align-items:center}
.arrow{width:32px;display:flex;justify-content:center}
.thumb-row{display:flex;gap:8px;margin-left:4px}
.thumb{width:122px;height:79px;border:4px solid #8a2a14;box-shadow:0 0 0 1px #5a1a0a}

.welcome-panel{position:absolute;left:142px;top:653px;width:587px;height:433px;background:linear-gradient(#eef2e2,#e0e8ce);border-top:1px solid #c6ccb4}
.welcome h1{font-family:"Josefin Sans",sans-serif;font-weight:300;font-size:30px;color:#4a3c32;position:absolute;left:21px;top:22px}
.welcome p{position:absolute;left:22px;top:60px;width:684px;font-size:10.5px;line-height:15px;text-indent:32px;width:550px;color:#7a7266}
.more{color:var(--olive);font-style:italic}
.divider-h{position:absolute;left:0;top:160px;width:587px;height:1px;background:#bfc4b0}
.divider-v{position:absolute;left:327px;top:185px;width:1px;height:225px;background:#c0c4b4}
.section-title{position:absolute;font-family:"Josefin Sans",sans-serif;font-size:18px;color:#6a5444;border-bottom:1px solid #a89a88}
.blurb{position:absolute;font-size:10.5px;line-height:15px;color:#7a7266}
.photo{position:absolute;border-radius:8px;border:1px solid #c0b8a8}
.badge{position:absolute;width:106px;height:107px;border:3px solid #4a9a3a;background:#f6f8f0}

.booking{position:absolute;left:734px;top:653px;width:260px;height:433px;background:var(--panel-dark);border-radius:4px;color:var(--white);font-family:"Arimo",sans-serif}
.booking h2{font-family:"Josefin Sans",sans-serif;font-weight:400;font-size:27px;color:var(--gold);text-align:center;padding-top:12px;height:46px}
.band{background:var(--panel-band);font-family:"Dancing Script",cursive;font-size:14px;color:#d8c8a8;padding:3px 10px;height:26px}
.field{display:flex;align-items:center;justify-content:space-between;padding:0 8px;height:26px;font-size:11.5px}
.field input{width:138px;height:20px;border:1px solid #bbb;background:var(--white);font-family:"Rosarivo",serif;font-size:11px;padding:0 4px;color:#555}
.date{display:flex;width:140px;height:21px;background:var(--white);border:1px solid #aaa}
.date span{flex:1;font-family:"Rosarivo",serif;font-size:11px;color:#444;padding:3px 4px}
.date i{width:22px;background:linear-gradient(#c8ccd6,#8a90a0)}
.note{font-family:"Rosarivo",serif;font-size:9px;color:var(--orange);text-align:right;padding:2px 8px}
.actions{display:flex;justify-content:center;gap:34px;padding:12px 0 6px;background:var(--panel-band);margin-top:8px;height:50px}
.btn{width:72px;height:30px;border-radius:4px;background:linear-gradient(#d8643a,#a8321a);font-family:"Josefin Sans",sans-serif;font-size:20px;color:var(--gold);display:flex;align-items:center;justify-content:center}
.agent{font-family:"Rosarivo",serif;font-size:11px;color:var(--orange);padding:14px 8px 0 14px;display:flex;align-items:center;gap:10px}
.agent b{width:8px;height:8px;background:var(--white);display:inline-block}

.site-footer{position:absolute;left:0;top:1098px;width:1138px;height:102px;background:linear-gradient(#a4472c,#7a2410);color:#f4ece4;text-align:center;font-size:11px;line-height:15px;padding-top:18px}
.site-footer .copy{margin-top:14px}
.site-footer a{color:#f4ece4}
</style>
</head>
<body>

<header class="site-header">
  <div class="brand">Corwith Lodge</div>
  <p class="tagline">“Lorem ipsum dolor sit amet, consectetur adipisicing elit, sed do eiusmod tempor incididunt”</p>
  <div class="social"><span></span><span></span></div>
</header>

<nav class="main-nav">
  <ul>
    <li class="active" style="width:89px">Home</li>
    <li style="width:100px">About The Lodge</li>
    <li style="width:88px">Rooms</li>
    <li style="width:102px">The Reservation</li>
    <li style="width:91px">Amenities</li>
    <li style="width:105px">Aspen Information</li>
    <li style="width:115px">Manager's Journal</li>
    <li style="width:79px">Webcams</li>
    <li style="width:84px">Contact Us</li>
  </ul>
</nav>

<section class="hero">
  <div class="hero-photo" role="img" aria-label="Rotating photo of the lodge exterior in winter snow">
    <div class="offer">
      <h2>SPECIAL OFFER</h2>
      <h3>Stay 3 nights, get the 4th night FREE!</h3>
      <p>Depending on the season, enjoy a huge range of activities from skiing, skating, fly-fishing, hiking, horseback riding, hang-gliding, music festival, food and wine show, comedy festival, winterskol, dog sled rides, (<a href="#">Read More</a>)</p>
    </div>
  </div>
  <div class="thumbs">
    <div class="arrow"><svg width="14" height="16"><path d="M14 0 L0 8 L14 16Z" fill="#b8361a"/></svg></div>
    <div class="thumb-row">
      <div class="thumb" role="img" aria-label="Guest room with iron bed" style="background:linear-gradient(#c8a878,#6a5040)"></div>
      <div class="thumb" role="img" aria-label="Guest room with wooden furniture" style="background:linear-gradient(#b88a5a,#5a3a28)"></div>
      <div class="thumb" role="img" aria-label="Guest room with carved bed" style="background:linear-gradient(#9a7a5a,#4a3022)"></div>
      <div class="thumb" role="img" aria-label="Dining room" style="background:linear-gradient(#b89878,#5a4030)"></div>
      <div class="thumb" role="img" aria-label="Lounge with fireplace" style="background:linear-gradient(#a88868,#3a2a22)"></div>
      <div class="thumb" role="img" aria-label="Lobby with flower display" style="background:linear-gradient(#8a4a3a,#3a2420)"></div>
    </div>
    <div class="arrow" style="margin-left:6px"><svg width="14" height="16"><path d="M0 0 L14 8 L0 16Z" fill="#b8361a"/></svg></div>
  </div>
</section>

<main class="welcome-panel">
  <div class="welcome">
    <h1>Welcome !</h1>
    <p>Located in the heart of downtown Aspen, the newly renovated Corwith Lodge possesses all the charms of a vintage European Ski Lodge, while offering all of the modern conveniences one would expect with a stay in Aspen. A stay at our lodge includes free continental breakfast in our dining room, daily maid service, free wireless internet access, and a fully-equipped conference facility. Guests are also invited to relax in one of our two outdoor Jacuzz is or in our lounge, where a 42-inch plasma TV and fireplace make for a pleasant area to unwind. <span class="more">Read More...</span></p>
  </div>
  <div class="divider-h"></div>
  <div class="divider-v"></div>

  <h2 class="section-title" style="left:27px;top:185px">Our Services</h2>
  <p class="blurb" style="left:15px;top:223px;width:150px">"Lorem ipsum dolor sit amet, consectetur adipisicing elit, sed do eiusmod tempor incid-idunt ut labore et dolore magna aliqua" <span class="more">Read More</span></p>
  <div class="photo" role="img" aria-label="Wood-panelled conference room" style="left:169px;top:212px;width:145px;height:93px;background:linear-gradient(#7a4a28,#c07a3a)"></div>
  <div class="photo" role="img" aria-label="Snowy mountain landscape" style="left:12px;top:322px;width:145px;height:93px;background:linear-gradient(#7aa8d8,#e8eef4)"></div>
  <p class="blurb" style="left:170px;top:332px;width:150px">"Lorem ipsum dolor sit amet, consectetur adipisicing elit, sed do eiusmod tempor incid-idunt ut labore et dolore magna aliqua" <span class="more">Read More</span></p>

  <h2 class="section-title" style="left:349px;top:185px">Achievement</h2>
  <p class="blurb" style="left:342px;top:214px;width:230px;text-indent:22px">Consectetur adipisicing elit, sed do eiusmod tempor incididunt ut labore et dolore magna aliqua. Duis aute irure dolor in reprehenderit in voluptate velit esse cillum dolore eu fugiat nulla pariatur. Excepteur sint occaecat cupidatat non proident," <span class="more">Read More</span></p>
  <div class="badge" style="left:348px;top:312px"></div>
  <div class="badge" style="left:463px;top:312px;background:#dcecd0"></div>
</main>

<aside class="booking">
  <h2>Book A Room</h2>
  <div class="band">Arrival and Departure Information</div>
  <div style="padding-top:8px">
    <div class="field">Check-in Date <div class="date"><span>Desember - 09 - 2012</span><i></i></div></div>
    <div class="field">Check-Out Date <div class="date"><span>Desember - 12 - 2012</span><i></i></div></div>
  </div>
  <div class="band" style="margin-top:8px">Room Information</div>
  <div style="padding:6px 0">
    <div class="field">Adult <input type="text" aria-label="Adult"></div>
    <div class="field">Children <input type="text" aria-label="Children"></div>
  </div>
  <div class="band">Rate Information</div>
  <div style="padding-top:8px">
    <div class="field">Rate <input type="text" aria-label="Rate"></div>
    <div class="field">Promotional Code <input type="text" aria-label="Promotional Code"></div>
    <p class="note">* All discount rates verified at check-in.</p>
  </div>
  <div class="actions"><span class="btn">Next</span><span class="btn">Check</span></div>
  <div class="agent"><b></b>Travel Agent &nbsp;(Agent Id &amp; Password Required)</div>
</aside>

<footer class="site-footer">
  <p>Corwith Lodge Hotel 418 W. Larkspur Street Aspen, CO 81611</p>
  <p>Call 970-555-0142 to contact the hotel. Toll Free: 877-555-0198</p>
  <p class="copy">© 2012 Corwith Lodge</p>
  <p><a href="#">privacy policy</a> &nbsp;| &nbsp;<a href="#">terms of use</a></p>
</footer>

</body>
</html>
```